Natural Skincare brand needs new labels!

We are a natural and organic skin care brand based in the united states. We are looking for unique product label designs that will help our brand stand out. We want the labels to look elegant and natural, but also incorporate some color. We want a design aspect like a line drawing on the labels, see examples. Please refer to our website to see our current labels and to get more of a feel of who we are. Our logo is included. We are looking for 5 labels for 5 different Products.
1. Body butter: 1.5"x9" rectangle wrap around 12oz jar with black lid
2. Eczema Salve: 1.5" circle silver metal tin
3. Glow Serum: 1.5"x3" rectangle Blue Dropper Bottle with black top
4. Mineral Mist: 1.5"x3" clear glass sprayer bottle (want clear label)
website: www.velmirabotanics.com
Instagram: @velmirabotanics

```html
<!DOCTYPE html>
<html lang="en">
<head>
<meta charset="utf-8">
<title>Velmira Label Set</title>
<link href="https://fonts.googleapis.com/css2?family=Questrial&family=Raleway:wght@700&display=swap" rel="stylesheet">
<style>
  :root {
    --canvas: #eaeaea;
    --paper: #ffffff;
    --blush: #f4b19c;
    --coral: #ef7b6b;
    --ink: #1d1d1d;
    --leaf-tint: #fbe6de;
    --shadow: 0 2px 5px rgba(0,0,0,0.22);
  }
  * { box-sizing: border-box; margin: 0; padding: 0; }
  html, body { width: 1200px; height: 1200px; overflow: hidden; }
  body {
    background: var(--canvas);
    font-family: "Questrial", "Century Gothic", sans-serif;
    color: var(--ink);
    position: relative;
  }

  .brand-name {
    font-family: "Questrial", sans-serif;
    color: var(--coral);
    letter-spacing: 0.02em;
    line-height: 1;
    display: flex;
    align-items: center;
    gap: 6px;
    white-space: nowrap;
  }
  .brand-dot {
    display: inline-block;
    border-radius: 50%;
    background: var(--coral);
  }

  .leaf-field {
    position: absolute;
    background: radial-gradient(ellipse at 55% 45%, var(--leaf-tint) 0%, rgba(251,230,222,0) 70%);
    opacity: 0.8;
  }

  /* Eczema salve tins */
  .salve-lid {
    position: absolute;
    top: 70px;
    width: 164px;
    height: 164px;
    border-radius: 50%;
    background: var(--paper);
    box-shadow: var(--shadow);
    overflow: hidden;
    display: flex;
    flex-direction: column;
    align-items: center;
  }
  .salve-lid--blush { background: var(--blush); }
  .salve-lid .leaf-field { inset: 0; border-radius: 50%; }
  .salve-lid .brand-name { font-size: 22px; margin-top: 30px; position: relative; }
  .salve-lid .brand-dot { width: 8px; height: 8px; }
  .salve-title { font-size: 14px; margin-top: 20px; position: relative; }
  .salve-rule { width: 64px; height: 1px; background: var(--ink); margin-top: 5px; position: relative; }
  .salve-claim { font-size: 8px; margin-top: 8px; position: relative; }
  .salve-size { font-size: 5.5px; margin-top: 4px; position: relative; }

  /* Body butter wrap */
  .butter-wrap {
    position: absolute;
    left: 108px; top: 379px;
    width: 986px; height: 163px;
    background: var(--paper);
    box-shadow: var(--shadow);
    overflow: hidden;
  }
  .butter-wrap .leaf-field { left: 340px; top: 0; width: 265px; height: 163px; }
  .butter-ingredients {
    position: absolute; left: 27px; top: 35px;
    font-size: 14.5px; line-height: 19px; text-transform: uppercase;
  }
  .label-heading { font-family: "Raleway", sans-serif; font-weight: 700; }
  .butter-brand {
    position: absolute; left: 360px; top: 0; width: 232px; height: 163px;
  }
  .butter-brand .brand-name {
    position: absolute; left: 0; right: 0; top: 48px;
    justify-content: center;
    font-size: 44px;
  }
  .butter-brand .brand-dot { width: 14px; height: 14px; }
  .scent-name {
    position: absolute; left: 0; right: 0; top: 133px;
    text-align: center;
    font-size: 15px; letter-spacing: 0.08em;
  }
  .butter-band {
    position: absolute; left: 605px; top: 0; width: 141px; height: 163px;
    background: var(--blush); color: var(--paper);
    display: flex; justify-content: center; align-items: center; gap: 14px;
  }
  .vertical-text { writing-mode: vertical-rl; transform: rotate(180deg); white-space: nowrap; }
  .butter-band .product-title { font-size: 22px; letter-spacing: 0.02em; }
  .butter-band .product-claim { font-size: 9.5px; }
  .butter-band .product-size { font-size: 7px; }
  .butter-usage {
    position: absolute; left: 770px; top: 53px;
    font-size: 14.5px; line-height: 19px; text-transform: uppercase;
  }

  /* Glow serum labels */
  .serum-label {
    position: absolute; top: 689px;
    width: 328px; height: 163px;
    background: var(--paper);
    box-shadow: var(--shadow);
    overflow: hidden;
  }
  .serum-label .leaf-field { left: 121px; top: 0; width: 207px; height: 163px; }
  .serum-band {
    position: absolute; left: 0; top: 0; width: 121px; height: 163px;
    background: var(--blush); color: var(--paper);
    display: flex; justify-content: center; align-items: center; gap: 10px;
  }
  .serum-band .product-title { font-size: 18px; }
  .serum-band .rule-v { width: 1px; height: 70px; background: var(--paper); margin-top: -40px; }
  .serum-band .product-claim { font-size: 9px; }
  .serum-band .product-size { font-size: 7px; }
  .serum-brand { position: absolute; left: 160px; top: 36px; }
  .serum-brand .brand-name { font-size: 32px; }
  .serum-brand .brand-dot { width: 11px; height: 11px; }
  .serum-scent { position: absolute; left: 182px; top: 106px; font-size: 14px; line-height: 16px; letter-spacing: 0.04em; }

  /* Mineral mist clear label */
  .mist-label {
    position: absolute; left: 500px; top: 1030px; width: 200px;
    display: flex; flex-direction: column; align-items: center;
  }
  .mist-label .brand-name { font-size: 36px; }
  .mist-label .brand-dot { width: 12px; height: 12px; }
  .mist-title { font-size: 13px; margin-top: 18px; }
  .mist-rule { width: 72px; height: 1px; background: var(--ink); margin-top: 3px; }
</style>
</head>
<body>

  <section class="salve-set" aria-label="Eczema Salve tin lids">
    <div class="salve-lid salve-lid--blush" style="left:275px;">
      <div class="leaf-field" role="img" aria-label="Faint line-drawn leaf pattern"></div>
      <div class="brand-name"><span class="brand-dot"></span>Velmira</div>
      <div class="salve-title">Eczema Salve</div>
      <div class="salve-rule"></div>
      <div class="salve-claim">Healing &amp; Regenrating</div>
      <div class="salve-size">1 oz/29 g</div>
    </div>
    <div class="salve-lid" style="left:518px;">
      <div class="leaf-field" role="img" aria-label="Faint line-drawn leaf pattern"></div>
      <div class="brand-name"><span class="brand-dot"></span>Velmira</div>
      <div class="salve-title">Eczema Salve</div>
      <div class="salve-rule"></div>
      <div class="salve-claim">Healing &amp; Regenrating</div>
      <div class="salve-size">1 oz/29 g</div>
    </div>
    <div class="salve-lid" style="left:762px;">
      <div class="leaf-field" role="img" aria-label="Faint line-drawn leaf pattern"></div>
      <div class="brand-name"><span class="brand-dot"></span>Velmira</div>
      <div class="salve-title">Eczema Salve</div>
      <div class="salve-rule"></div>
      <div class="salve-claim">Healing &amp; Regenrating</div>
      <div class="salve-size">1 oz/29 g</div>
    </div>
  </section>

  <section class="butter-wrap" aria-label="Body butter jar wrap">
    <div class="leaf-field" role="img" aria-label="Faint line-drawn leaf pattern"></div>
    <div class="butter-ingredients">
      <div class="label-heading">Ingredients:</div>
      Shea butter,mango butter<br>
      Kokum butter,coconut oil<br>
      Sesame oil, vitamin E oil<br>
      Essential oils
    </div>
    <div class="butter-brand">
      <div class="brand-name"><span class="brand-dot"></span>Velmira</div>
      <div class="scent-name">LAVENDER</div>
    </div>
    <div class="butter-band">
      <div class="vertical-text product-title">Body butter</div>
      <div class="vertical-text product-claim">Moisturizing &amp; Nourishing</div>
      <div class="vertical-text product-size">12 oz/340 g</div>
    </div>
    <div class="butter-usage">
      <div class="label-heading">How to use:</div>
      Apply all over body<br>
      as a daily moisturizer.
    </div>
  </section>

  <section class="serum-label" style="left:226px;" aria-label="Glow Serum label">
    <div class="leaf-field" role="img" aria-label="Faint line-drawn leaf pattern"></div>
    <div class="serum-band">
      <div class="vertical-text product-title">Glow Serum</div>
      <div class="rule-v"></div>
      <div class="vertical-text product-claim">Glow Even Skin Tone</div>
      <div class="vertical-text product-size">2 oz</div>
    </div>
    <div class="serum-brand"><div class="brand-name"><span class="brand-dot"></span>Velmira</div></div>
    <div class="serum-scent">Manjistha &amp;<br>Safflower</div>
  </section>

  <section class="serum-label" style="left:648px;" aria-label="Glow Serum label">
    <div class="leaf-field" role="img" aria-label="Faint line-drawn leaf pattern"></div>
    <div class="serum-band">
      <div class="vertical-text product-title">Glow Serum</div>
      <div class="rule-v"></div>
      <div class="vertical-text product-claim">Glow Even Skin Tone</div>
      <div class="vertical-text product-size">2 oz</div>
    </div>
    <div class="serum-brand"><div class="brand-name"><span class="brand-dot"></span>Velmira</div></div>
    <div class="serum-scent">Manjistha &amp;<br>Safflower</div>
  </section>

  <section class="mist-label" aria-label="Mineral Mist clear label">
    <div class="brand-name"><span class="brand-dot"></span>Velmira</div>
    <div class="mist-title">Mineral Mist</div>
    <div class="mist-rule"></div>
  </section>

</body>
</html>
```